Tavish Advisory Partners Business Card Design Project

2-sided business card for my small (me and a couple subcontractors) firm, which consults to public community colleges and school districts and public agencies in California on energy matters, mostly solar electric systems that can reduce their electricity use by as much as 80%. I prepare requests for proposals (RFPs), manage the RFP processes, and work with the solar vendors to get the best deal for my clients. I also do regulatory and legislative advocacy for strong renewable energy policies. I do lots of quantitative analysis to make sure the solar systems are sized to produce the maximum monetary savings and focus a lot on the aesthetic design of the solar systems, as architectural features of the campuses (most are carport structures built in parking lots, but some are built on the ground and on rooftops). All my work is geared to getting the best value, highest quality, and most reliable solar system. My career background is in public interest energy advocacy; I'm not a consultant trying to make a million dollars but someone who is still serving in the public interest.

My competition is made up of much larger firms; this business card/logo in large part is intended to present an image of my firm as an equal to these larger firms despite my smaller size.

Essential information as follows:
Firm name: Tavish Advisory Partners
Tagline: Clean Energy Procurement for the Public Sector
Name: Bennet Okafor
email, 2 phone number, and address listed as well.

Target Market(s)

Public schools, community colleges, & public agencies.There is a wide range in the sophistication of these organizations.

Industry/Entity Type

Parking

Requirements
Must have
• - several rich colors, which can be either in the logo or in the background - the overall feeling of the card should reflect richness of color. I have uploaded some photos showing some colors that I like together. By rich I do not necessarily mean bright. I suppose bright colors in the logo could be supported with rich colors in the overall background of the card.
- professional, and powerful in an understated way (not kooky, cartoonish, or very playful)
- the logo must NOT be too representational of solar energy or the sun, but at the same time it would be good for the logo to be somewhat suggestive of this.

Nice to have
• -I like abstract and geometric images (with rich colts).
- A very subtle reference to schools/colleges/education would be great but it CANNOT be explicit; it would have to be faintly suggestive.
- In the logo I like the idea of abstract or geometric shapes intersecting with other in an interesting and suggestive way, conveying the multiple aspects of my practice (economics, data analysis, energy analysis, problem solving, managing collaborative processes, policy analysis)
- My work relates to environmental concerns, especially climate change. Working this into the logo in a subtle way could be good, but it's not a requirement.
- I like the idea that the logo/card feels serene.
- In designing the business card, I kind of like the idea of having the tag line as the first thing they read, then they see the firm name.

Should not have
• Not:
- humorous
- boring
- overly slick
- overly formal
- whimsical

```html
<!DOCTYPE html>
<html lang="en">
<head>
<meta charset="utf-8">
<title>Tavish Advisory Partners – Business Card</title>
<link rel="stylesheet" href="https://fonts.googleapis.com/css2?family=Arimo:wght@400;700&display=swap">
<style>
  :root {
    --page: #c9c9c9;
    --navy-deep: #071642;
    --navy-mid: #0d2a6e;
    --navy-glow: #2a5cae;
    --white: #ffffff;
    --paper: #fbfbfb;
    --cyan: #0aa0cb;
    --ink: #2b2b2b;
    --ink-soft: #555555;
    --rule: #9a9a9a;
  }
  * { box-sizing: border-box; margin: 0; padding: 0; }
  html, body {
    width: 1200px; height: 1010px; overflow: hidden;
    background: var(--page);
    font-family: "Arimo", Arial, sans-serif;
  }
  .sheet {
    position: relative; width: 1200px; height: 1010px;
    display: flex; align-items: center; justify-content: center; gap: 40px;
  }
  .card {
    position: relative; width: 540px; height: 333px; overflow: hidden;
    border-radius: 22px 0 22px 0;
  }

  /* Front */
  .card--front {
    background: radial-gradient(ellipse 70% 55% at 50% 100%, var(--navy-glow) 0%, var(--navy-mid) 45%, var(--navy-deep) 100%);
    color: var(--white);
    text-align: center;
  }
  .front__mark {
    position: absolute; left: 225px; top: 72px;
    width: 90px; height: 90px; background: var(--white);
  }
  .front__name {
    position: absolute; left: 0; right: 0; top: 186px;
    font-size: 28px; font-weight: 700; letter-spacing: -0.3px;
  }
  .front__tagline {
    position: absolute; left: 0; right: 0; top: 222px;
    font-size: 12.5px; font-weight: 700;
  }
  .front__rule {
    position: absolute; left: 130px; width: 280px; top: 280px; height: 2px;
    background: linear-gradient(90deg, transparent, rgba(255,255,255,0.85) 30%, rgba(255,255,255,0.85) 70%, transparent);
  }
  .front__web {
    position: absolute; left: 0; right: 0; top: 295px;
    font-size: 14px;
  }

  /* Back */
  .card--back { background: var(--paper); color: var(--ink); }
  .back__mark {
    position: absolute; left: 58px; top: 60px;
    width: 52px; height: 52px; background: var(--cyan);
  }
  .back__divider {
    position: absolute; left: 142px; top: 44px; width: 1px; height: 88px;
    background: var(--rule);
  }
  .back__name {
    position: absolute; left: 155px; top: 70px;
    font-size: 20px; font-weight: 700; color: var(--ink); letter-spacing: -0.3px;
  }
  .back__tagline {
    position: absolute; left: 155px; top: 96px;
    font-size: 8.5px; color: var(--ink-soft);
  }
  .back__bar {
    position: absolute; right: 0; top: 62px; width: 125px; height: 58px;
    background: var(--cyan);
  }
  .person { position: absolute; left: 51px; top: 186px; }
  .person__name { font-size: 18px; font-weight: 700; }
  .person__title { font-size: 13.5px; color: var(--ink-soft); margin-top: 2px; }
  .contact { position: absolute; left: 51px; top: 243px; list-style: none; font-size: 13.5px; line-height: 19px; color: var(--ink); }
  .back__corner { position: absolute; right: 0; bottom: 0; }
</style>
</head>
<body>
<main class="sheet">
  <section class="card card--front" aria-label="Card front">
    <div class="front__mark"></div>
    <h1 class="front__name">Tavish Advisory Partners</h1>
    <p class="front__tagline">Clean Energy Procurement for the Public Sector</p>
    <div class="front__rule"></div>
    <p class="front__web">www.tavishadvisory.com</p>
  </section>

  <section class="card card--back" aria-label="Card back">
    <div class="back__mark"></div>
    <div class="back__divider"></div>
    <h2 class="back__name">Tavish Advisory Partners</h2>
    <p class="back__tagline">Clean Energy Procurement for the Public Sector</p>
    <div class="back__bar"></div>

    <div class="person">
      <p class="person__name">Bennet Okafor</p>
      <p class="person__title">Manging Partner</p>
    </div>
    <ul class="contact">
      <li>email : bennet@tavishadvisory.com</li>
      <li>ph : 000-000-0000</li>
      <li>address : street address</li>
    </ul>

    <svg class="back__corner" width="200" height="150" viewBox="0 0 200 150" aria-hidden="true">
      <rect x="0" y="0" width="200" height="150" fill="#0aa0cb"/>
    </svg>
  </section>
</main>
</body>
</html>
```